Larkspur Ridge Management - Business Cards

I need business cards. My current logo was designed by a designer at this site and I very much like and am happy with the results. I would like a business card that is trendy, unique, current yet professional. I deal with high net worth clients daily

Target Market(s)

Out of state investors looking to get into the rental market in Ohio

Industry/Entity Type

Property Management, Consulting

Contact Information for Business Card

Name, Title (Chief Financial Officer) office phone number (555) 817-3094 website address larkridgemgmt.example

Font styles to use
Sans Serif

Colors
0054AA
0677BA
7BADD7
CADEEF
E8F1F8
0094D4
00A9DD
6FCCEA
C7EBF8
E9F6FB
00AB8E
00BBA5
67D7C9
C6EFE9
E9F9F6

```html
<!DOCTYPE html>
<html lang="en">
<head>
<meta charset="utf-8">
<title>Larkspur Ridge Management – Business Cards</title>
<link rel="stylesheet" href="https://fonts.googleapis.com/css2?family=Montserrat:wght@500;600;700&display=swap">
<style>
  :root {
    --navy: #1b2a4a;
    --red: #c8232c;
    --paper: #f4f4f4;
    --ink: #1b2a4a;
    --stage: #2e2f31;
    --white: #ffffff;
  }
  * { margin: 0; padding: 0; box-sizing: border-box; }
  html, body {
    width: 1200px;
    height: 1200px;
    overflow: hidden;
    background: var(--stage);
    font-family: "Montserrat", sans-serif;
  }
  .card-set {
    position: relative;
    width: 1200px;
    height: 1200px;
  }
  .card {
    position: absolute;
    top: 446px;
    width: 540px;
    height: 309px;
    overflow: hidden;
  }
  .card-front { left: 40px; background: var(--paper); }
  .card-back { left: 620px; background: var(--navy); }

  .front-shapes { position: absolute; inset: 0; }

  .emboss-area {
    position: absolute;
    left: 245px;
    top: 28px;
    width: 270px;
    height: 200px;
    background: linear-gradient(160deg, #fafafa 0%, #ececec 100%);
  }

  .identity { position: absolute; left: 34px; top: 58px; }
  .person-name {
    font-size: 25px;
    font-weight: 700;
    color: var(--ink);
    letter-spacing: 0.5px;
    line-height: 1;
  }
  .person-title {
    margin-top: 9px;
    font-size: 12.5px;
    font-weight: 500;
    color: var(--red);
    letter-spacing: 0.4px;
  }
  .title-rule {
    margin-top: 12px;
    width: 50px;
    height: 4px;
    background: linear-gradient(to bottom, var(--red) 0 50%, var(--navy) 50% 100%);
  }

  .contact-list {
    position: absolute;
    left: 34px;
    top: 142px;
    list-style: none;
  }
  .contact-item {
    display: flex;
    align-items: center;
    gap: 10px;
    height: 22px;
    margin-bottom: 11px;
    font-size: 14px;
    font-weight: 500;
    color: var(--ink);
  }
  .contact-icon { width: 22px; height: 22px; flex: none; }

  .tagline {
    position: absolute;
    left: 34px;
    top: 243px;
    font-size: 13px;
    font-weight: 500;
    color: var(--white);
    letter-spacing: 0.6px;
    line-height: 1.5;
  }

  .brand-name {
    position: absolute;
    inset: 0;
    display: flex;
    align-items: center;
    justify-content: center;
    text-align: center;
    font-size: 30px;
    font-weight: 700;
    color: var(--white);
    letter-spacing: 1px;
    line-height: 1.25;
    padding: 0 60px;
  }
</style>
</head>
<body>
<main class="card-set">

  <section class="card card-front" aria-label="Business card front">
    <div class="emboss-area" role="img" aria-label="Blind-embossed brand symbol on white stock"></div>

    <svg class="front-shapes" viewBox="0 0 540 309" width="540" height="309" aria-hidden="true">
      <polygon fill="var(--navy)" points="0,198 262,198 290,232 488,232 512,198 540,198 540,309 0,309"/>
      <polygon fill="var(--red)" points="372,296 540,290 540,309 364,309"/>
    </svg>

    <div class="identity">
      <h1 class="person-name">YOUR NAME</h1>
      <p class="person-title">CHIEF FINANCIAL OFFICER</p>
      <div class="title-rule"></div>
    </div>

    <ul class="contact-list">
      <li class="contact-item">
        <svg class="contact-icon" viewBox="0 0 22 22" aria-hidden="true">
          <circle cx="11" cy="11" r="11" fill="var(--navy)"/>
          <path fill="var(--white)" d="M7.6 5.6c.4-.3 1-.2 1.3.2l1.2 1.8c.3.4.2.9-.1 1.2l-.8.7c.6 1.3 1.6 2.4 2.9 3l.7-.8c.3-.4.9-.4 1.2-.1l1.8 1.2c.4.3.5.9.2 1.3l-.7 1c-.5.7-1.4.9-2.2.6-3.2-1.2-5.6-3.7-6.7-6.9-.3-.8 0-1.7.6-2.2z"/>
        </svg>
        <span>(555) 817-3094</span>
      </li>
      <li class="contact-item">
        <svg class="contact-icon" viewBox="0 0 22 22" aria-hidden="true">
          <circle cx="11" cy="11" r="11" fill="var(--navy)"/>
          <g fill="none" stroke="var(--white)" stroke-width="1">
            <circle cx="11" cy="11" r="6"/>
            <ellipse cx="11" cy="11" rx="2.6" ry="6"/>
            <line x1="5" y1="11" x2="17" y2="11"/>
            <line x1="6" y1="8" x2="16" y2="8"/>
            <line x1="6" y1="14" x2="16" y2="14"/>
          </g>
        </svg>
        <span>larkridgemgmt.example</span>
      </li>
    </ul>

    <p class="tagline">EXPERT MANAGEMENT.<br>STRONGER RETURNS.</p>
  </section>

  <section class="card card-back" aria-label="Business card back">
    <p class="brand-name">Larkspur Ridge Management</p>
  </section>

</main>
</body>
</html>
```